Marlo Tidy Yard Website

We need a website design for this new company. I've attached the company logo. This company is in the construction industry that provides general labor, maintenance and cleaning for construction sites. We want a clean and simple website that can be easy to navigate.

Target Market(s)

Construction industry

Industry/Entity Type

Construction

Number of Pages Required

2 page

Font styles to use
Sans Serif

```html
<!DOCTYPE html>
<html lang="en">
<head>
<meta charset="utf-8">
<title>Marlo Tidy Yard — Website and Cards</title>
<link href="https://fonts.googleapis.com/css2?family=Open+Sans:ital,wght@0,400;0,600;0,700;0,800;1,400;1,600&display=swap" rel="stylesheet">
<style>
:root{
  --orange:#f26522;
  --navy:#25215e;
  --navy-deep:#1e1a5c;
  --ink:#333338;
  --grey-text:#555;
  --band:#e6e6e8;
  --footer:#efeff0;
  --white:#fff;
}
*{margin:0;padding:0;box-sizing:border-box}
html,body{width:1200px;height:1200px;overflow:hidden;background:var(--white)}
body{position:relative;font-family:'Open Sans',sans-serif;color:var(--ink)}
.abs{position:absolute}
.photo{position:absolute}

/* website */
.site{position:absolute;left:103px;top:48px;width:576px;height:1084px;background:var(--white);outline:1px solid #ddd}
.hero{left:103px;top:48px;width:576px;height:252px;background:linear-gradient(180deg,#2a2a2c,#48494b 60%,#2c2c2e)}
.topbar{top:62px;font-size:8px;color:var(--white);line-height:10px}
.social{display:inline-block;width:9px;height:9px;background:var(--white);margin-left:2px;vertical-align:-1px}
.nav{left:132px;top:102px;width:526px;height:48px;background:var(--white)}
.brand{font-weight:800;color:var(--navy);line-height:1}
.nav .brand{position:absolute;left:22px;top:11px;font-size:11px;width:60px}
.nav-item{position:absolute;top:15px;font-size:14px;color:var(--ink)}
.hero-title{left:103px;width:576px;top:172px;text-align:center;color:var(--white);font-size:24px;font-weight:600}
.hero-sub{left:200px;width:382px;top:208px;text-align:center;color:var(--white);font-size:8.4px;font-weight:700;line-height:12px}

.h-section{font-size:16px;color:#222}
.h-section em{font-style:normal;color:var(--orange)}
.rule{height:1px;background:var(--orange)}
.body-text{font-size:6.6px;line-height:10px;color:var(--grey-text)}
.orange-label{font-size:8px;font-style:italic;color:var(--orange)}
.tag{position:absolute;height:18px;border:1px solid #999;font-size:6.5px;font-style:italic;text-align:center;line-height:16px;color:#222}
.tile{position:absolute;width:155px;height:114px}
.more-btn{left:321px;top:857px;width:140px;height:19px;border:1px solid var(--orange);color:var(--orange);font-style:italic;font-size:9.5px;line-height:17px;padding-left:5px}

.newsletter{left:103px;top:897px;width:576px;height:50px;background:var(--band)}
.news-title{font-size:7px;font-weight:700;color:#555}
.news-text{font-size:6.5px;line-height:12px;color:#555}
.email-field{left:386px;top:915px;width:235px;height:21px;background:var(--white);font-size:8px;font-style:italic;color:#999;padding:5px 11px}
.send-btn{left:625px;top:915px;width:30px;height:21px;background:var(--orange)}

.footer{left:103px;top:947px;width:576px;height:145px;background:var(--footer)}
.footer-head{font-size:12.5px;color:#222}
.footer-text{font-size:5.8px;font-weight:700;line-height:8.5px;color:#222;text-align:justify}
.thumb{position:absolute;width:31px;height:21px}
.mini-title{font-size:5px;font-style:italic;font-weight:700;color:var(--navy)}
.mini-text{font-size:3.6px;line-height:4.4px;color:#555}
.mini-more{font-size:3.8px;color:var(--orange)}
.contact-line{font-size:7.2px;line-height:11px;color:#333}
.contact-line b{font-weight:400;color:var(--orange)}
.social-o{position:absolute;top:1074px;width:11px;height:11px;background:var(--orange)}
.copyright{left:103px;width:576px;top:1103px;text-align:center;font-size:10px;font-style:italic;color:#222}

/* cards */
.card{position:absolute;left:738px;width:377px;height:212px}
.card-front{top:365px;background:var(--white);outline:1px solid #ddd}
.card-back{top:630px;background:radial-gradient(circle at 50% 45%,#2d2876,var(--navy-deep) 70%)}
.card-name{font-size:17px;color:var(--navy)}
.card-name em{font-style:normal;color:var(--orange)}
.card-text{font-size:8.4px;line-height:12px;color:#222}
.card-contact{font-size:8.4px;color:#222}
</style>
</head>
<body>

<div class="site"></div>

<!-- hero -->
<div class="photo hero" role="img" aria-label="Industrial plant at dusk with towers and pipework, dark toned"></div>
<div class="abs topbar" style="left:136px">
  <svg width="9" height="9" viewBox="0 0 10 10" style="vertical-align:-1px"><path d="M2 1l2 2-1 1.5c.6 1.2 1.3 1.9 2.5 2.5L7 6l2 2-1.5 1.5C4.5 9 1 5.5.5 2.5z" fill="#fff"/></svg>
  000.000.00000 | 000.000.00000
</div>
<div class="abs topbar" style="left:507px">LOG IN</div>
<div class="abs topbar" style="left:547px">Follow us on<span class="social"></span><span class="social"></span><span class="social"></span><span class="social"></span></div>

<nav class="abs nav">
  <div class="brand">Marlo Tidy Yard</div>
  <span class="nav-item" style="left:125px">Home</span>
  <span class="nav-item" style="left:208px">About US</span>
  <span class="nav-item" style="left:313px">Our Service</span>
  <span class="nav-item" style="left:430px">Contact US</span>
</nav>

<h1 class="abs hero-title">CONSTRUCTION SITE MAINTENANCE</h1>
<p class="abs hero-sub">Over 40 Years of combined construction experience, Marlo Tidy Yard, LLC recognizes the need for Housekeeping and General Industry Hygiene to maintain a Safe and Productive Construction Site.</p>

<!-- welcome -->
<h2 class="abs h-section" style="left:126px;top:318px;font-weight:400">WELCOME TO &nbsp;<em>MARLO</em></h2>
<div class="abs rule" style="left:287px;top:327px;width:138px"></div>
<p class="abs body-text" style="left:126px;top:351px;width:326px">Marlo Tidy Yard, LLC is the Metroplex's Premier Provider of Construction Site Maintenance for all sizes and types of construction projects. Our Strong Core Values of Safety, Quality, and Customer Satisfaction set us apart as a leader in the Construction Site Maintenance Industry. With over 40 Years of combined construction experience, Marlo Tidy Yard, LLC recognizes the need for House-keeping and General Industry Hygiene to maintain a Safe and Productive Construction Site. A Clean Site is a safe site, and Safety is our #1 goal.</p>
<p class="abs orange-label" style="left:126px;top:418px">Our services include</p>
<p class="abs body-text" style="left:126px;top:432px;width:330px">General Site Labor, Janitorial Services, Site Logistics, Site Office Set Up, Lawncare Maintenance, Landscape and Maintenance, Dumpster Services, Debris Removal</p>
<div class="abs" style="left:480px;top:340px;width:126px;height:117px;border-left:1px solid #aaa;border-bottom:1px solid #aaa"></div>
<div class="photo" style="left:488px;top:335px;width:167px;height:114px;background:linear-gradient(135deg,#8d8a86,#c9a66b 55%,#d96a2a)" role="img" aria-label="Construction site with concrete mixer truck and worker in hard hat and safety vest"></div>

<!-- services -->
<div class="abs rule" style="left:126px;top:491px;width:64px"></div>
<h2 class="abs h-section" style="left:201px;top:481px;font-weight:400">OUR <em>SERVICE</em></h2>
<span class="tag" style="left:127px;top:512px;width:73px">General Site Labor</span>
<span class="tag" style="left:208px;top:512px;width:74px">Janitorial Services</span>
<span class="tag" style="left:288px;top:512px;width:70px">Site Logistics</span>
<span class="tag" style="left:367px;top:512px;width:73px">Site Office Set Up</span>
<span class="tag" style="left:447px;top:512px;width:88px">Lowncare Maintenance</span>
<span class="tag" style="left:540px;top:512px;width:109px">Landscape and Maintenance</span>
<span class="tag" style="left:127px;top:542px;width:85px">Dumpster Services</span>
<span class="tag" style="left:222px;top:542px;width:67px">Debris Removal</span>

<div class="tile" style="left:125px;top:578px;background:linear-gradient(135deg,#d9d6d2,#b7a48a)" role="img" aria-label="Site labor crew reviewing plans"></div>
<div class="tile" style="left:310px;top:578px;background:linear-gradient(135deg,#b9c6d4,#5a6f9a)" role="img" aria-label="Janitorial staff cleaning an office"></div>
<div class="tile" style="left:495px;top:578px;background:linear-gradient(135deg,#d7dbe0,#a49a86)" role="img" aria-label="Engineer with plans at a logistics yard"></div>
<div class="tile" style="left:125px;top:721px;background:linear-gradient(135deg,#5f9a3a,#3d7425)" role="img" aria-label="Worker mowing a lawn"></div>
<div class="tile" style="left:310px;top:721px;background:linear-gradient(135deg,#4f7fa8,#a35a33)" role="img" aria-label="Crew loading a dumpster truck"></div>
<div class="tile" style="left:495px;top:721px;background:linear-gradient(135deg,#c9a27a,#6b5644)" role="img" aria-label="Excavator clearing demolition debris"></div>

<div class="abs more-btn">View all our project
  <svg width="34" height="6" viewBox="0 0 34 6" style="vertical-align:1px;margin-left:4px"><path d="M0 3h32M28 0l4 3-4 3" stroke="#f26522" fill="none" stroke-width="1"/></svg>
</div>

<!-- newsletter -->
<div class="abs newsletter"></div>
<p class="abs news-title" style="left:146px;top:902px">News Letter</p>
<p class="abs news-text" style="left:146px;top:917px">Our company has performed in a cleaning construction site,<br>General labour maintenence and proffesional matter</p>
<div class="abs email-field">your email</div>
<div class="abs send-btn">
  <svg width="30" height="21" viewBox="0 0 30 21"><path d="M9 11l12-5-3 10-3-3zM15 13l-1 3" fill="#fff"/></svg>
</div>

<!-- footer -->
<div class="abs footer"></div>
<div class="abs brand" style="left:153px;top:980px;font-size:13px;width:100px">Marlo Tidy Yard</div>
<p class="abs footer-text" style="left:151px;top:1031px;width:108px">Marlo Tidy Yard, LLC is the Metroplex's Premier Provider of Construction Site Maintenance for all sizes and types of construction projects.</p>
<span class="social-o" style="left:151px"></span>
<span class="social-o" style="left:168px"></span>
<span class="social-o" style="left:185px"></span>
<span class="social-o" style="left:200px"></span>

<h3 class="abs footer-head" style="left:319px;top:976px;font-weight:400">Our Service</h3>
<div class="abs rule" style="left:319px;top:994px;width:14px"></div>
<div class="thumb" style="left:318px;top:1005px;background:linear-gradient(135deg,#d9d6d2,#b7a48a)" role="img" aria-label="Site labor crew"></div>
<p class="abs mini-title" style="left:354px;top:1000px">General Site Labor</p>
<p class="abs mini-text" style="left:354px;top:1007px;width:84px">Site crews keep work areas clear, safe and ready for each new shift.</p>
<p class="abs mini-more" style="left:354px;top:1024px">View more</p>
<div class="thumb" style="left:318px;top:1048px;background:linear-gradient(135deg,#c9a27a,#6b5644)" role="img" aria-label="Debris removal"></div>
<p class="abs mini-title" style="left:354px;top:1043px">Debris Removal</p>
<p class="abs mini-text" style="left:354px;top:1050px;width:84px">Waste and scrap are hauled off site on a set weekly schedule.</p>
<p class="abs mini-more" style="left:354px;top:1067px">View more</p>

<h3 class="abs footer-head" style="left:516px;top:976px;font-weight:400">Contact Us</h3>
<div class="abs rule" style="left:516px;top:994px;width:14px"></div>
<p class="abs contact-line" style="left:518px;top:1001px"><b>Address:</b> Dummy city<br>Dummy Country, Land</p>
<p class="abs contact-line" style="left:518px;top:1032px"><b>Tel :</b> 000.000.0000<br><b>Fax:</b> 000.000.0000</p>
<p class="abs contact-line" style="left:518px;top:1063px"><b>Email:</b> info@marlo.com</p>

<p class="abs copyright">Copyright Marlo Tidy Yard. All right reserved</p>

<!-- business card front -->
<div class="card card-front"></div>
<div class="abs brand" style="left:793px;top:442px;font-size:24px;width:122px;line-height:26px">Marlo Tidy Yard</div>
<div class="abs" style="left:921px;top:411px;width:1px;height:124px;background:var(--orange)"></div>
<p class="abs card-name" style="left:938px;top:409px"><em>Evan</em> Hale</p>
<p class="abs card-text" style="left:938px;top:433px">Director</p>
<p class="abs card-text" style="left:938px;top:454px">Dummy city<br>Dummy Country Land</p>
<svg class="abs" style="left:933px;top:490px" width="10" height="40" viewBox="0 0 10 40">
  <path d="M1 3c2-2 6-2 8 0v1.5H7V3.5H3v1H1zM2 5h6l1 3H1z" fill="#f26522"/>
  <circle cx="5" cy="20" r="4" fill="#f26522"/><path d="M1 20h8M5 16v8" stroke="#fff" stroke-width=".7"/>
  <rect x="1" y="31" width="8" height="6" fill="#f26522"/><path d="M1 31l4 3 4-3" stroke="#fff" stroke-width=".7" fill="none"/>
</svg>
<p class="abs card-contact" style="left:948px;top:488px">000.000.0000</p>
<p class="abs card-contact" style="left:948px;top:503px">www.marlotidyyard.com</p>
<p class="abs card-contact" style="left:948px;top:518px">evan@marlotidyyard.com</p>

<!-- business card back -->
<div class="card card-back"></div>
<div class="abs brand" style="left:738px;width:377px;top:712px;text-align:center;font-size:30px;color:var(--white)">Marlo Tidy Yard</div>

</body>
</html>
```